Quimby's Yard & Garden Center Business Card Update

I need an updated Business card design for my Lawn and Garden Center. We do Landscaping installs, Lawn Mowing, Snow Removal and also have a Garden Center Retail Division. I uploaded a few of our previous business cards to give an idea of what we are starting with. The main goal of this update is to simplify and modernize the business card, not all of the services that are on the previous cards has to be on the new one but I would still like to highlight our main services. There is also a sample of our logo that Can be used in the design.

Industry/Entity Type

Landscaping

Contact Information for Business Card

Morris Quimby
Morris@Quimbysyardandgarden.example
Business (555) 201-7784
Cell (555) 318-6092

Colors

Designer to choose colors to be used in the design.

Requirements
Must have
• Services Provided :
• Landscaping
• Lawn Maintenance
• Snow Removal
• Garden Center

```html
<!DOCTYPE html>
<html lang="en">
<head>
<meta charset="utf-8">
<title>Quimby's Yard &amp; Garden Center — Business Card</title>
<link href="https://fonts.googleapis.com/css2?family=Oswald:wght@500;600&family=Poppins:wght@600&family=Barlow:wght@500;600&display=swap" rel="stylesheet">
<style>
  :root {
    --green: #0b5a35;
    --green-light: #1a6e45;
    --card-white: #ededed;
    --pill-white: #f2f2f2;
    --ink-grey: #6b6b6b;
    --backdrop: #d9d9d9;
  }
  * { box-sizing: border-box; margin: 0; padding: 0; }
  html, body { width: 1200px; height: 900px; overflow: hidden; }
  body {
    background: var(--backdrop);
    position: relative;
    font-family: "Barlow", sans-serif;
  }
  .card {
    position: absolute;
    left: 250px;
    width: 700px;
    height: 400px;
    border-radius: 6px;
    overflow: hidden;
    box-shadow: 0 8px 24px rgba(0,0,0,0.18);
  }

  /* Front */
  .card-front {
    top: 30px;
    background: linear-gradient(160deg, var(--green) 0%, var(--green-light) 100%);
    color: var(--pill-white);
  }
  .front-brand {
    position: absolute;
    left: 0; right: 0; top: 92px;
    text-align: center;
    font-family: "Poppins", sans-serif;
    font-weight: 600;
    color: var(--pill-white);
    line-height: 1.1;
  }
  .front-brand .brand-name { font-size: 64px; display: block; }
  .front-brand .brand-sub { font-size: 22px; letter-spacing: 0.3em; display: block; margin-top: 6px; }
  .services-title {
    position: absolute;
    left: 0; right: 0; top: 268px;
    text-align: center;
    font-family: "Oswald", sans-serif;
    font-weight: 600;
    font-size: 22px;
    letter-spacing: 0.04em;
    text-transform: uppercase;
    white-space: nowrap;
  }
  .services-pill {
    position: absolute;
    left: 30px; right: 30px; top: 318px;
    height: 40px;
    padding: 0 24px;
    border-radius: 20px;
    background: var(--pill-white);
    color: var(--green);
    display: flex;
    align-items: center;
    justify-content: center;
    gap: 12px;
    font-family: "Oswald", sans-serif;
    font-weight: 600;
    font-size: 19px;
    line-height: 1;
    letter-spacing: 0.01em;
    text-transform: uppercase;
    white-space: nowrap;
  }
  .services-pill span { flex: 0 0 auto; }
  .services-pill .divider { font-weight: 500; }

  /* Back */
  .card-back {
    top: 470px;
    background: var(--card-white);
  }
  .back-brand-tab {
    position: absolute;
    left: 160px; top: 0;
    width: 380px; height: 170px;
    background: var(--green);
    border-radius: 0 0 18px 18px;
    display: flex;
    flex-direction: column;
    align-items: center;
    justify-content: center;
    font-family: "Poppins", sans-serif;
    font-weight: 600;
    color: var(--pill-white);
    line-height: 1.15;
  }
  .back-brand-tab .brand-name { font-size: 40px; }
  .back-brand-tab .brand-sub { font-size: 14px; letter-spacing: 0.25em; }
  .contact {
    position: absolute;
    left: 0; right: 0; top: 196px;
    text-align: center;
    color: var(--ink-grey);
    white-space: nowrap;
  }
  .contact-name {
    font-family: "Poppins", sans-serif;
    font-weight: 600;
    font-size: 30px;
    margin-bottom: 10px;
  }
  .contact-line {
    font-weight: 600;
    font-size: 21px;
    letter-spacing: 0.03em;
    line-height: 1.4;
  }
  .contact-line .gap { display: inline-block; width: 22px; }
  .contact-web {
    margin-top: 12px;
    font-weight: 600;
    font-size: 16px;
    letter-spacing: 0.04em;
    color: var(--green);
  }
</style>
</head>
<body>

<section class="card card-front" aria-label="Card front">
  <div class="front-brand">
    <span class="brand-name">Quimby's</span>
    <span class="brand-sub">YARD &amp; GARDEN CENTER</span>
  </div>
  <div class="services-title">Services Provided</div>
  <div class="services-pill">
    <span>Landscaping</span><span class="divider">/</span>
    <span>Lawn Maintenance</span><span class="divider">/</span>
    <span>Snow Removal</span><span class="divider">/</span>
    <span>Garden Center</span>
  </div>
</section>

<section class="card card-back" aria-label="Card back">
  <div class="back-brand-tab">
    <span class="brand-name">Quimby's</span>
    <span class="brand-sub">YARD &amp; GARDEN CENTER</span>
  </div>
  <div class="contact">
    <p class="contact-name">Morris Quimby</p>
    <p class="contact-line">M. (555) 318-6092<span class="gap"></span>T. (555) 201-7784</p>
    <p class="contact-line">482 Orchard Lane, Millbrook, Ohio 45999</p>
    <p class="contact-line">Morris@Quimbysyardandgarden.example</p>
    <p class="contact-web">www.quimbysyardandgarden.example</p>
  </div>
</section>

</body>
</html>
```